Packaging artwork design for furniture

Currently our packaging is utilitarian. We want a new look that reflects our new exciting branding strategy. We want the packaging to reflect a sophisticated, expensive look. I have attached the current packaging and the logo. All the information on the box are required for the new design.
Please use between 2-3 colours, not more.

Target Market(s)

International

Industry/Entity Type

furniture

Requirements
Must have
• All the symbols but need some extra artwork
Nice to have
• artwork that portrays high end, expensive look

```html
<!DOCTYPE html>
<html lang="en">
<head>
<meta charset="utf-8">
<title>Hearthwell Night Table Carton</title>
<link href="https://fonts.googleapis.com/css2?family=Cinzel:wght@500&family=Saira+Semi+Condensed:wght@600&display=swap" rel="stylesheet">
<style>
  :root {
    --kraft: #b68d62;
    --kraft-light: #c69f74;
    --kraft-dark: #a57d54;
    --ink: #2f2f2f;
    --paper: #ffffff;
  }
  * { box-sizing: border-box; margin: 0; padding: 0; }
  html, body { width: 1200px; height: 1200px; overflow: hidden; background: var(--paper); }
  .canvas {
    position: relative; width: 1200px; height: 1200px;
    display: flex; align-items: center; justify-content: center;
  }
  .carton { display: flex; }
  .panel {
    position: relative; height: 588px;
    background: linear-gradient(180deg, var(--kraft-dark) 0%, var(--kraft) 45%, var(--kraft-light) 100%);
    color: var(--ink);
  }
  .panel--front { width: 560px; border-right: 1px solid rgba(0,0,0,.12); }
  .panel--side {
    width: 426px;
    display: flex; flex-direction: column; align-items: center;
    padding: 52px 36px 40px;
  }
  .base-band { position: absolute; left: 0; right: 0; bottom: 0; height: 40px; background: var(--ink); }

  .brand {
    display: flex; align-items: center; justify-content: center; gap: 12px;
    font-family: "Cinzel", serif; font-weight: 500; color: var(--ink); letter-spacing: .04em; line-height: 1;
  }
  .brand__square { background: var(--ink); flex: none; }
  .panel--front .brand { position: absolute; left: 0; right: 0; top: 272px; font-size: 34px; }
  .panel--front .brand__square { width: 22px; height: 22px; }
  .panel--side .brand { font-size: 24px; }
  .panel--side .brand__square { width: 16px; height: 16px; }

  .this-way-up { position: absolute; top: 28px; right: 30px; width: 74px; height: 86px; }
  .corner-mark { position: absolute; left: 50%; bottom: 92px; width: 52px; height: 52px; margin-left: -26px; background: var(--ink); }

  .spec-table {
    margin-top: 140px; width: 354px; border-collapse: collapse;
    font-family: "Saira Semi Condensed", sans-serif; font-weight: 600; font-size: 20px; color: var(--ink);
  }
  .spec-table td { border: 1.5px solid var(--ink); height: 42px; padding: 0 16px; letter-spacing: .02em; }
  .spec-table td:first-child { width: 48%; }
  .dimensions {
    margin-top: 30px; text-align: center; line-height: 1;
    font-family: "Saira Semi Condensed", sans-serif; font-weight: 600; font-size: 20px;
  }
  .handling { margin-top: 26px; width: 354px; display: flex; justify-content: space-between; }
  .handling svg { width: 42px; height: 50px; display: block; }
</style>
</head>
<body>
<main class="canvas">
  <div class="carton">
    <section class="panel panel--front">
      <svg class="this-way-up" viewBox="0 0 74 86" aria-label="This way up">
        <rect x="2" y="2" width="70" height="82" rx="6" fill="none" stroke="var(--ink)" stroke-width="3"/>
        <path d="M26 62V24M48 62V24" stroke="var(--ink)" stroke-width="5"/>
        <path d="M17 30l9-14 9 14zM39 30l9-14 9 14z" fill="var(--ink)"/>
        <rect x="16" y="66" width="42" height="5" fill="var(--ink)"/>
      </svg>
      <div class="brand"><span class="brand__square"></span>Hearthwell</div>
      <div class="corner-mark"></div>
      <div class="base-band"></div>
    </section>

    <section class="panel panel--side">
      <div class="brand"><span class="brand__square"></span>Hearthwell</div>
      <table class="spec-table">
        <tr><td>MODEL</td><td>HW204-NT07</td></tr>
        <tr><td>ITEM</td><td>Night Table</td></tr>
        <tr><td>QUANTITY</td><td>1/1</td></tr>
        <tr><td>CBM</td><td></td></tr>
      </table>
      <p class="dimensions">625x475x655</p>
      <div class="handling">
        <svg viewBox="0 0 44 52" aria-label="This way up"><rect x="1.5" y="1.5" width="41" height="49" rx="4" fill="none" stroke="var(--ink)" stroke-width="2"/><path d="M16 38V16M28 38V16" stroke="var(--ink)" stroke-width="3"/><path d="M11 19l5-8 5 8zM23 19l5-8 5 8z" fill="var(--ink)"/><rect x="10" y="40" width="24" height="3" fill="var(--ink)"/></svg>
        <svg viewBox="0 0 44 52" aria-label="Fragile"><rect x="1.5" y="1.5" width="41" height="49" rx="4" fill="none" stroke="var(--ink)" stroke-width="2"/><path d="M14 12h16l-2 12a6 6 0 0 1-12 0z" fill="var(--ink)"/><path d="M22 30v10M16 41h12" stroke="var(--ink)" stroke-width="2.5"/></svg>
        <svg viewBox="0 0 44 52" aria-label="Keep dry"><rect x="1.5" y="1.5" width="41" height="49" rx="4" fill="none" stroke="var(--ink)" stroke-width="2"/><path d="M9 26a13 11 0 0 1 26 0z" fill="var(--ink)"/><path d="M22 26v12a3 3 0 0 1-6 0" fill="none" stroke="var(--ink)" stroke-width="2"/></svg>
        <svg viewBox="0 0 44 52" aria-label="Handle with care"><rect x="1.5" y="1.5" width="41" height="49" rx="4" fill="none" stroke="var(--ink)" stroke-width="2"/><rect x="15" y="12" width="14" height="12" fill="var(--ink)"/><path d="M10 20v12l7 8M34 20v12l-7 8" fill="none" stroke="var(--ink)" stroke-width="3.5"/></svg>
        <svg viewBox="0 0 44 52" aria-label="Keep away from fire"><rect x="1.5" y="1.5" width="41" height="49" rx="4" fill="none" stroke="var(--ink)" stroke-width="2"/><path d="M22 10c8 8 12 14 12 22a12 11 0 0 1-24 0c0-6 3-9 5-12 1 4 3 6 5 6-2-6 0-11 2-16z" fill="var(--ink)"/></svg>
        <svg viewBox="0 0 44 52" aria-label="Recyclable"><rect x="1.5" y="1.5" width="41" height="49" rx="4" fill="none" stroke="var(--ink)" stroke-width="2"/><path d="M22 13l10 17H12z" fill="none" stroke="var(--ink)" stroke-width="3.5"/><path d="M30 26l4 6-7 1zM17 10l5 1-2 6z" fill="var(--ink)"/></svg>
      </div>
      <div class="base-band"></div>
    </section>
  </div>
</main>
</body>
</html>
```